Vellmora Harvest Online organic artisan and gourmet supermarket

Brief:
Brand: Vellmora Harvest (VH) is an online store selling artisan and organinc Italian products. Our look and feel we have gone with is rustic, premium and unfiltered (visit us @ www.vellmoraharvest.com.au)
Our slogan: "cook Italy, eat Italy, love Italy"
Goals: prior to our online store going live, we used to attend a food market once a week. Due to unfortunate circumstances, we stopped. Since then, our store has gone live and wanted to use the card as a reminder we are back at the markets.
I also have a restaurant, "vellmora ristorante" so I wanted to hand them out to customers in the restaurant but also act as reminder of our pop up market stores and our website to buy from.
Personality: VH is more than just a store. Our goal is to be not only a store but an informationa hub of Italian food.
We offer assistance to people who need help in their kitchen as well as catering
Logo: I have a logo which I was not able to upload.

Target Market(s)

Food lovers
Italian food interest
Wealthy
Organic gourmet food enthusiest

Industry/Entity Type

Store

Contact Information for Business Card

Shop online or visit us @ Birchwell Hollow organic market
Ciao@vellmoraharvest.com.au
Www.vellmoraharvest.com.au

Online store, Cooking advice, catering, ristorante and information hub

Requirements
Must have
• Logo
• Information
• May be larger than a business card to fit information but smaller than a post card
• Need to look interesting and different
• Not a simple card design
Nice to have
• Different fonts
• Rustic looking
• Qwerky

```html
<!DOCTYPE html>
<html lang="en">
<head>
<meta charset="utf-8">
<title>Vellmora Harvest — Business Card</title>
<link rel="stylesheet" href="https://fonts.googleapis.com/css2?family=PT+Serif:ital,wght@0,400;1,400&display=swap">
<style>
  :root {
    --page-bg: #3a3a3a;
    --card-dark: #1b1b1b;
    --card-light: #f3f3f3;
    --card-light-shade: #e2e2e2;
    --ink-light: #f2f2f2;
    --ink-dark: #1e1e1e;
    --tab-white: #ffffff;
  }
  * { margin: 0; padding: 0; box-sizing: border-box; }
  html, body { width: 1200px; height: 750px; overflow: hidden; }
  body {
    background: var(--page-bg);
    font-family: "PT Serif", Georgia, serif;
    position: relative;
  }
  .card {
    position: absolute;
    top: 228px;
    width: 462px;
    height: 263px;
    border-radius: 14px;
    overflow: hidden;
  }
  .card--back { left: 124px; background: var(--card-dark); color: var(--ink-light); }
  .card--front { left: 618px; color: var(--ink-dark); }

  .card__texture {
    position: absolute; inset: 0;
    background:
      radial-gradient(ellipse at 15% 85%, var(--card-light-shade) 0%, transparent 45%),
      radial-gradient(ellipse at 85% 20%, var(--card-light-shade) 0%, transparent 40%),
      var(--card-light);
  }

  .tab {
    position: absolute;
    left: 50%;
    width: 66px; height: 66px;
    margin-left: -33px;
    border-radius: 50%;
    background: var(--tab-white);
  }
  .tab--top { top: -33px; }
  .tab--bottom { bottom: -33px; }

  .contact {
    position: absolute;
    left: 0; right: 0; top: 62px;
    text-align: center;
    font-style: italic;
    font-size: 14px;
    line-height: 16px;
  }
  .contact__group { margin-bottom: 8px; }

  .brand {
    position: absolute;
    left: 166px; top: 23px;
    width: 138px; height: 138px;
    border: 1.5px solid var(--ink-dark);
    border-radius: 50%;
    display: flex; align-items: center; justify-content: center;
    text-align: center;
  }
  .brand__name {
    font-size: 15px;
    line-height: 19px;
    letter-spacing: 1.5px;
    text-transform: uppercase;
    color: var(--ink-dark);
  }
  .slogan {
    position: absolute; left: 0; right: 0; top: 170px;
    text-align: center;
    font-size: 14.5px;
    letter-spacing: 0.6px;
  }
  .services {
    position: absolute; left: 0; right: 0; top: 191px;
    text-align: center;
    font-size: 12.5px;
    line-height: 15.5px;
  }
  .social {
    position: absolute; left: 0; right: 0; top: 227px;
    display: flex; align-items: center; justify-content: center; gap: 3px;
  }
  .social__rule { width: 58px; height: 1px; background: var(--ink-dark); margin: 0 4px; }
  .social__dot {
    width: 20px; height: 20px;
    border: 1.2px solid var(--ink-dark);
    border-radius: 50%;
  }
</style>
</head>
<body>
  <section class="card card--back" aria-label="Card back">
    <div class="tab tab--top"></div>
    <div class="contact">
      <p class="contact__group">48 Larkmoor St<br>Denhollow, 2187</p>
      <p class="contact__group">Shop online or visit us<br>@ Birchwell Hollow organic market</p>
      <p class="contact__group">Ph : (02) 5550 1827<br>Ciao@vellmoraharvest.com.au<br>www.vellmoraharvest.com.au</p>
    </div>
    <div class="tab tab--bottom"></div>
  </section>

  <section class="card card--front" aria-label="Card front">
    <div class="card__texture" role="img" aria-label="Rustic distressed light grey paper texture"></div>
    <div class="brand"><span class="brand__name">Vellmora<br>Harvest</span></div>
    <p class="slogan">COOK ITALY, EAT ITALY, LOVE ITALY</p>
    <p class="services">Online store &bull; Cooking advice<br>Catering &bull; Ristorante and information hub</p>
    <div class="social">
      <span class="social__rule"></span>
      <span class="social__dot"></span>
      <span class="social__dot"></span>
      <span class="social__dot"></span>
      <span class="social__rule"></span>
    </div>
  </section>
</body>
</html>
```